Business and Success Coaching Business Card

Need a business card for my coaching business. I coach small businesses, career professionals and, individuals wanting to unlock their human potential and achieve excellence. At the heart of our methodology is the Shaping Purposeful Action Routines Knowingly (SPARK) approach to formulate empowerment, create principles for success and setting achievable outcomes. I would like something that incorporates our new logo, something clean and sharp with a solid darker, but complementary background, color on the card front. The back should be white where there will be room for three questions

Target Market(s)

People looking to advance and improve themselves through a success coach

Industry/Entity Type

Life Coaching

Contact Information for Business Card

Contact information on card.
Business name on front of card
Questions on back

Font styles to use
Other font styles liked:
• Century Gothic or other Serif style fonts that look similar to Century Gothic

Colors

Designer to choose colors to be used in the design.

Requirements
Must have
• Logo on front of card
• Business name - The Steady Forge
• Contact name - Ted Harlow
• Address - Box 4619, Cedar Hollow, WA 98011-4619
• Phone number - 303-555-0147
• Email address - harlow.ted@thesteadyforge.example
• Certifications - CAC, CRP, PTC, PSB
• Back of card
• Three questions on the back of the card:
• If you were at your best, what would you do right now?
• What is the decision you have been avoiding?
• What's one action you could take in the next 10 minutes?
Nice to have
• I would like to see a solid color on the front of the card that compliments the logo.
• Back should be white, or could be contrasting, but need to have the three questions.

```html
<!DOCTYPE html>
<html lang="en">
<head>
<meta charset="utf-8">
<title>The Steady Forge – Business Card</title>
<link rel="stylesheet" href="https://fonts.googleapis.com/css2?family=Open+Sans:wght@700&family=Didact+Gothic&display=swap">
<style>
  :root {
    --page: #ffffff;
    --card: #ffffff;
    --frame: #3a3a3a;
    --accent-gold: #fbc02d;
    --navy: #2e3466;
    --brand-navy: #1f3a6e;
    --ink-blue: #2a4577;
    --icon-blue: #4a86c8;
    --rule-blue: #5b9bd5;
    --ink: #141414;
  }
  * { margin: 0; padding: 0; box-sizing: border-box; }
  html, body { width: 1200px; height: 1000px; overflow: hidden; background: var(--page); }
  .canvas { position: relative; width: 1200px; height: 1000px; }

  .card {
    position: absolute;
    left: 212px;
    width: 795px;
    height: 454px;
    background: var(--card);
    border: 1px solid var(--frame);
    border-top: 2px solid #555;
  }
  .card::before, .card::after {
    content: "";
    position: absolute;
    left: 0; right: 0;
    height: 8px;
    background: var(--accent-gold);
  }
  .card::before { top: 0; }
  .card::after { bottom: 0; }

  .card-front { top: 38px; }
  .card-back { top: 507px; }

  .brand-name {
    position: absolute;
    right: 57px;
    top: 153px;
    font: 700 30px/1 "Open Sans", sans-serif;
    color: var(--brand-navy);
    letter-spacing: -0.2px;
  }

  .holder-name {
    position: absolute;
    left: 57px;
    top: 172px;
    font: 700 29px/1 "Open Sans", sans-serif;
    color: var(--navy);
    text-transform: uppercase;
    letter-spacing: 0.2px;
  }
  .name-rule {
    position: absolute;
    left: 57px;
    top: 219px;
    width: 682px;
    height: 2px;
    background: var(--rule-blue);
  }

  .contact-list { list-style: none; position: absolute; left: 57px; top: 238px; }
  .contact-item {
    display: flex;
    align-items: center;
    height: 47px;
    font: 25px/1 "Didact Gothic", sans-serif;
    color: var(--ink-blue);
  }
  .contact-icon { width: 28px; height: 30px; margin-right: 7px; flex: none; }

  .certifications {
    position: absolute;
    left: 0; right: 0;
    top: 398px;
    padding-left: 18px;
    text-align: center;
    font: 25px/1 "Didact Gothic", sans-serif;
    color: var(--ink-blue);
  }
  .certifications em { font-style: italic; }

  .question {
    position: absolute;
    left: 36px;
    font: 24px/1 "Didact Gothic", sans-serif;
    color: var(--ink);
  }
  .q1 { top: 44px; }
  .q2 { top: 167px; }
  .q3 { top: 303px; }
</style>
</head>
<body>
<div class="canvas">

  <section class="card card-front" aria-label="Card front">
    <div class="brand-name">The Steady Forge</div>

    <h1 class="holder-name">Ted Harlow</h1>
    <div class="name-rule"></div>

    <ul class="contact-list">
      <li class="contact-item">
        <svg class="contact-icon" viewBox="0 0 28 30" aria-hidden="true">
          <rect x="5" y="1" width="15" height="28" rx="2.5" fill="var(--icon-blue)"/>
          <rect x="7.5" y="5" width="10" height="18" fill="#fff"/>
          <circle cx="12.5" cy="26" r="1.2" fill="#fff"/>
        </svg>
        303-555-0147
      </li>
      <li class="contact-item">
        <svg class="contact-icon" viewBox="0 0 28 30" aria-hidden="true" fill="none" stroke="var(--icon-blue)" stroke-width="1.4">
          <path d="M2 27 V17 a5 5 0 0 1 10 0 V27 Z"/>
          <path d="M7 12 H22 a4 4 0 0 1 4 4 V27 H12"/>
          <line x1="19" y1="12" x2="19" y2="2"/>
          <rect x="19" y="2" width="5" height="4"/>
          <line x1="4" y1="19" x2="9" y2="19"/>
        </svg>
        Box 4619, Cedar Hollow, WA 98011-4619
      </li>
      <li class="contact-item">
        <svg class="contact-icon" viewBox="0 0 28 30" aria-hidden="true" fill="none" stroke="var(--icon-blue)" stroke-width="1.4">
          <rect x="1" y="8" width="26" height="16"/>
          <path d="M1 8 L14 18 L27 8"/>
          <path d="M1 24 L11 15.5 M27 24 L17 15.5"/>
        </svg>
        harlow.ted@thesteadyforge.example
      </li>
    </ul>

    <p class="certifications">Certifications: <em>CAC, CRP, PTC, PSB</em></p>
  </section>

  <section class="card card-back" aria-label="Card back">
    <p class="question q1">If you were at your best, what would you do right now?</p>
    <p class="question q2">What is the decision you have been avoiding?</p>
    <p class="question q3">What's one action you could take in the next 10 minutes?</p>
  </section>

</div>
</body>
</html>
```